Web Developer Needs a Business Card Design

I need a personal business card design that represents me as a web developer for potential employers. I would like the background to be a dark color on the front for contrast with my logo and name. The back will have all my information along with a smaller version of the logo. I want something with a modern look and feel, not too conservative. This will be used for potential employers and freelance work.

Industry/Entity Type

Business

Contact Information for Business Card

Front should have my logo and name. The back should have all my personal information which would include: name: Tom Brevardi, phone: 570-614-9083, email: tombrevardi@mailwisp.com, website url: www.tombrevardi.com, logo, web developer.

Font styles to use
Sans Serif

Requirements
Must have
• Must include my logo. The color palette base color will be the logo color.

```html
<!DOCTYPE html>
<html lang="en">
<head>
<meta charset="utf-8">
<title>Tom Brevardi – Business Card</title>
<link rel="stylesheet" href="https://fonts.googleapis.com/css2?family=Fira+Sans:wght@600&family=Montserrat:wght@400;500;600&display=swap">
<style>
  :root {
    --page-bg: #e6e6e8;
    --card-dark: #3b3f46;
    --card-dark-light: #4d525a;
    --card-dark-deep: #30343a;
    --paper-white: #ffffff;
    --accent-teal: #5ee3c4;
    --ink-black: #1d1d1f;
    --text-light: #f2f3f4;
  }
  * { box-sizing: border-box; margin: 0; padding: 0; }
  html, body {
    width: 1200px;
    height: 900px;
    overflow: hidden;
    background: var(--page-bg);
  }
  .canvas {
    position: relative;
    width: 1200px;
    height: 900px;
  }
  .card {
    position: absolute;
    left: 320px;
    width: 560px;
    height: 320px;
    overflow: hidden;
    box-shadow: 0 10px 30px rgba(0, 0, 0, 0.18);
  }
  .card--back { top: 90px; }
  .card--front { top: 490px; }

  .dark-surface {
    background:
      repeating-linear-gradient(90deg,
        var(--card-dark-deep) 0px,
        var(--card-dark) 40px,
        var(--card-dark-light) 80px,
        var(--card-dark) 120px,
        var(--card-dark-deep) 160px);
  }

  /* back side */
  .back-header {
    position: absolute;
    left: 0; top: 0;
    width: 100%;
    height: 112px;
    background: var(--paper-white);
    display: flex;
    align-items: center;
    justify-content: center;
    gap: 14px;
  }
  .back-body {
    position: absolute;
    left: 0; top: 112px;
    width: 100%;
    height: 208px;
    display: flex;
    flex-direction: column;
    align-items: center;
    justify-content: center;
    gap: 12px;
  }
  .mark-ring {
    display: block;
    flex: none;
  }
  .identity { line-height: 1.2; }
  .identity__name {
    font-family: "Montserrat", sans-serif;
    font-weight: 600;
    font-size: 16px;
    color: var(--ink-black);
  }
  .identity__role {
    font-family: "Montserrat", sans-serif;
    font-weight: 400;
    font-size: 12px;
    color: var(--accent-teal);
    letter-spacing: 0.02em;
  }
  .contact-line {
    font-family: "Montserrat", sans-serif;
    font-weight: 400;
    font-size: 14px;
    color: var(--text-light);
    letter-spacing: 0.02em;
  }

  /* front side */
  .front-brand {
    position: absolute;
    right: 90px;
    top: 70px;
    display: flex;
    flex-direction: column;
    align-items: flex-end;
    gap: 18px;
  }
  .front-brand .mark-ring { margin-right: 40px; }
  .front-brand__name {
    font-family: "Fira Sans", sans-serif;
    font-weight: 600;
    font-size: 32px;
    color: var(--text-light);
    letter-spacing: 0.01em;
  }
</style>
</head>
<body>
  <main class="canvas">

    <section class="card card--back" aria-label="Business card back">
      <header class="back-header">
        <svg class="mark-ring" width="52" height="52" viewBox="0 0 52 52" aria-hidden="true">
          <circle cx="26" cy="26" r="22" fill="none" stroke="var(--accent-teal)" stroke-width="4"/>
        </svg>
        <div class="identity">
          <p class="identity__name">Tom Brevardi</p>
          <p class="identity__role">Web Developer</p>
        </div>
      </header>
      <div class="back-body dark-surface">
        <p class="contact-line">570-614-9083</p>
        <p class="contact-line">tombrevardi@mailwisp.com</p>
        <p class="contact-line">www.tombrevardi.com</p>
      </div>
    </section>

    <section class="card card--front dark-surface" aria-label="Business card front">
      <div class="front-brand">
        <svg class="mark-ring" width="120" height="120" viewBox="0 0 120 120" aria-hidden="true">
          <circle cx="60" cy="60" r="54" fill="none" stroke="var(--accent-teal)" stroke-width="7"/>
        </svg>
        <p class="front-brand__name">Tom Brevardi</p>
      </div>
    </section>

  </main>
</body>
</html>
```